Larkspur Ridge Management - Business Cards

I need business cards. My current logo was designed by a designer at this site and I very much like and am happy with the results. I would like a business card that is trendy, unique, current yet professional. I deal with high net worth clients daily

Target Market(s)

Out of state investors looking to get into the rental market in Ohio

Industry/Entity Type

Property Management, Consulting

Contact Information for Business Card

Name, Title (Chief Financial Officer) office phone number (555) 817-3094 website address larkridgemgmt.example

Font styles to use
Sans Serif

Colors
0054AA
0677BA
7BADD7
CADEEF
E8F1F8
0094D4
00A9DD
6FCCEA
C7EBF8
E9F6FB
00AB8E
00BBA5
67D7C9
C6EFE9
E9F9F6

```html
<!DOCTYPE html>
<html lang="en">
<head>
<meta charset="utf-8">
<title>Larkspur Ridge Management – Business Cards</title>
<link rel="stylesheet" href="https://fonts.googleapis.com/css2?family=Barlow+Semi+Condensed:wght@600;700&family=Roboto:wght@500&display=swap">
<style>
  :root {
    --blue-deep: #0054AA;
    --blue-mid: #0677BA;
    --blue-soft: #7BADD7;
    --blue-pale: #CADEEF;
    --blue-mist: #E8F1F8;
    --sky: #00A9DD;
    --sky-pale: #C7EBF8;
    --sky-mist: #E9F6FB;
    --teal: #00AB8E;
    --teal-light: #00BBA5;
    --teal-pale: #C6EFE9;
    --white: #ffffff;
  }
  * { box-sizing: border-box; margin: 0; padding: 0; }
  html, body {
    width: 1200px; height: 703px; overflow: hidden;
    background: var(--white);
  }
  .card {
    position: absolute; left: 15px; width: 1169px; height: 328px;
    overflow: hidden;
  }
  .card--front { top: 15px; background: var(--white); border: 1px solid var(--blue-mist); }
  .card--back { top: 359px; background: var(--sky-mist); border: 1px solid var(--blue-mist); }
  .card__shapes { position: absolute; inset: 0; width: 100%; height: 100%; }

  .wordmark {
    position: absolute; display: flex; flex-direction: column; align-items: center;
    font-family: "Barlow Semi Condensed", sans-serif; font-weight: 700;
    font-size: 38px; line-height: 1.02; text-align: center; letter-spacing: 0.5px;
  }
  .wordmark__dot { width: 42px; height: 42px; border-radius: 50%; margin-bottom: 12px; background: var(--teal); }
  .card--front .wordmark { left: 169px; top: 62px; width: 270px; color: var(--blue-deep); }
  .card--back .wordmark { left: 143px; top: 48px; width: 270px; color: var(--white); }

  .skyline {
    position: absolute; left: 1000px; top: 40px; width: 169px; height: 216px;
    background: linear-gradient(180deg, rgba(123,173,215,0.22), rgba(123,173,215,0));
  }

  .headline {
    position: absolute; left: 585px; top: 72px; width: 410px; text-align: center;
    font-family: "Barlow Semi Condensed", sans-serif; font-weight: 700;
    color: var(--white); font-size: 68px; line-height: 62px; letter-spacing: 0.5px;
  }
  .subhead {
    position: absolute; left: 583px; top: 198px; width: 412px; height: 36px;
    display: flex; align-items: center; gap: 12px;
    font-family: "Barlow Semi Condensed", sans-serif; font-weight: 700;
    color: var(--sky-pale); font-size: 31px; line-height: 36px; letter-spacing: 4px; white-space: nowrap;
  }
  .subhead__rule { flex: 1; height: 3px; background: var(--teal-light); }
  .tagline {
    position: absolute; left: 615px; top: 248px; width: 340px;
    font-family: "Roboto", sans-serif; font-weight: 500;
    color: var(--blue-mist); font-size: 14px; line-height: 20px; letter-spacing: 5.3px;
  }

  .person { position: absolute; left: 582px; top: 40px; }
  .person__name {
    font-family: "Barlow Semi Condensed", sans-serif; font-weight: 700;
    color: var(--blue-deep); font-size: 57px; line-height: 56px; letter-spacing: 0.5px;
    white-space: nowrap;
  }
  .person__rule { width: 78px; height: 4px; background: var(--teal); margin-top: 10px; }
  .person__title {
    margin-top: 12px;
    font-family: "Roboto", sans-serif; font-weight: 500;
    color: var(--blue-mid); font-size: 21px; letter-spacing: 1.6px;
  }
  .contact {
    position: absolute; left: 583px; top: 174px;
    display: grid; grid-template-columns: 38px 1px auto; column-gap: 18px; row-gap: 18px;
    align-items: center;
  }
  .contact__icon { width: 37px; height: 37px; }
  .contact__divider { grid-column: 2; grid-row: 1 / span 2; width: 2px; height: 92px; background: var(--teal); }
  .contact__text {
    font-family: "Roboto", sans-serif; font-weight: 500;
    color: var(--blue-deep); font-size: 24px;
  }
</style>
</head>
<body>

<section class="card card--front">
  <svg class="card__shapes" viewBox="0 0 1597 448" preserveAspectRatio="none" aria-hidden="true">
    <polygon points="0,0 215,0 0,210" fill="var(--blue-deep)"/>
    <line x1="0" y1="165" x2="165" y2="0" stroke="var(--white)" stroke-width="3"/>
    <polygon points="780,0 905,0 648,255 648,140" fill="var(--teal)"/>
    <polygon points="905,0 1597,0 1597,448 465,448 648,265 648,255" fill="var(--blue-deep)"/>
    <polygon points="1262,448 1360,360 1455,360 1360,448" fill="var(--sky)"/>
    <polygon points="1360,448 1480,318 1597,318 1597,448" fill="var(--blue-pale)"/>
  </svg>
  <div class="skyline" role="img" aria-label="Faint line drawing of city buildings"></div>

  <div class="wordmark">
    <span class="wordmark__dot"></span>
    <span>LARKSPUR RIDGE</span>
    <span>MANAGEMENT</span>
  </div>

  <h1 class="headline">PROPERTY<br>MANAGEMENT</h1>
  <div class="subhead"><span class="subhead__rule"></span>&amp; CONSULTING<span class="subhead__rule"></span></div>
  <p class="tagline">STRATEGIC SOLUTIONS.<br>STRONGER PROPERTIES.</p>
</section>

<section class="card card--back">
  <svg class="card__shapes" viewBox="0 0 1597 449" preserveAspectRatio="none" aria-hidden="true">
    <polygon points="1040,449 1308,175 1576,449" fill="var(--blue-mist)"/>
    <polygon points="1130,449 1308,265 1486,449" fill="var(--sky-mist)"/>
    <polygon points="0,0 770,0 690,95 690,285 525,449 240,449 0,240" fill="var(--blue-deep)"/>
    <polygon points="690,95 690,285 525,449 480,449 640,285 640,145" fill="var(--teal)"/>
    <polygon points="0,200 210,0 245,0 0,240" fill="var(--sky)"/>
    <line x1="0" y1="262" x2="226" y2="22" stroke="var(--white)" stroke-width="2.5"/>
    <line x1="648" y1="92" x2="740" y2="0" stroke="var(--white)" stroke-width="2.5"/>
    <polygon points="0,240 240,449 0,449" fill="var(--blue-pale)"/>
    <polygon points="1460,175 1597,35 1597,200 1460,340" fill="var(--teal)"/>
    <polygon points="1365,449 1597,215 1597,250 1400,449" fill="var(--blue-deep)"/>
    <line x1="1420" y1="449" x2="1597" y2="270" stroke="var(--blue-mid)" stroke-width="2.5"/>
  </svg>

  <div class="wordmark">
    <span class="wordmark__dot"></span>
    <span>LARKSPUR RIDGE</span>
    <span>MANAGEMENT</span>
  </div>

  <div class="person">
    <h2 class="person__name">DANIEL WHITAKER</h2>
    <div class="person__rule"></div>
    <p class="person__title">CHIEF FINANCIAL OFFICER</p>
  </div>

  <div class="contact">
    <svg class="contact__icon" viewBox="0 0 40 40" aria-hidden="true">
      <circle cx="20" cy="20" r="20" fill="var(--blue-deep)"/>
      <path d="M13 11c1-1 2.5-1 3.2 0l2 3c.6.9.4 2-.4 2.7l-1.3 1c.9 2.2 2.6 3.9 4.8 4.8l1-1.3c.7-.8 1.8-1 2.7-.4l3 2c1 .7 1 2.2 0 3.2l-1.3 1.3c-1.4 1.4-3.6 1.6-5.4.6-4.3-2.4-7.4-5.5-9.8-9.8-1-1.8-.8-4 .6-5.4z" fill="var(--white)"/>
    </svg>
    <span class="contact__divider"></span>
    <span class="contact__text">(555) 817-3094</span>
    <svg class="contact__icon" viewBox="0 0 40 40" aria-hidden="true">
      <circle cx="20" cy="20" r="20" fill="var(--blue-deep)"/>
      <g fill="none" stroke="var(--white)" stroke-width="1.6">
        <circle cx="20" cy="20" r="10"/>
        <ellipse cx="20" cy="20" rx="4.5" ry="10"/>
        <line x1="10" y1="20" x2="30" y2="20"/>
        <line x1="20" y1="10" x2="20" y2="30"/>
        <path d="M12 14.5h16M12 25.5h16"/>
      </g>
    </svg>
    <span class="contact__text">larkridgemgmt.example</span>
  </div>
</section>

</body>
</html>
```